Estou muito feliz om o resultado final do trabalho de vocês gostaria de agradecer a toda a equipe que me ajudou na construção desse projeto. Parabenizar em especial o MARCELO do 0800... muito solicito presta um ótimo atendimento.

```html
<!DOCTYPE html>
<html lang="pt-BR">
<head>
<meta charset="utf-8">
<title>Rafael Moura – Cartão de Visita</title>
<link href="https://fonts.googleapis.com/css2?family=Montserrat:wght@500;700;800&display=swap" rel="stylesheet">
<style>
  :root {
    --bg: #e9e4dc;
    --card: #1b1b1d;
    --card-edge: #111112;
    --red: #d8232a;
    --white: #ffffff;
    --muted: #d9d9d9;
  }
  * { box-sizing: border-box; margin: 0; padding: 0; }
  html, body { width: 1200px; height: 1200px; overflow: hidden; }
  body {
    background: var(--bg);
    font-family: "Montserrat", sans-serif;
    color: var(--white);
    position: relative;
  }
  .card {
    position: absolute;
    left: 150px;
    width: 900px;
    height: 510px;
    border-radius: 34px;
    background: var(--card);
    overflow: hidden;
    box-shadow: 0 14px 30px rgba(0,0,0,.18);
  }
  .card--back { top: 60px; }
  .card--front { top: 630px; }

  /* back */
  .back-accent { position: absolute; inset: 0; }
  .back-mark {
    position: absolute; top: 38px; right: 48px;
    width: 58px; height: 58px; border-radius: 50%;
    background: var(--white);
  }
  .contact-list { position: absolute; left: 60px; top: 56px; list-style: none; }
  .contact-item {
    display: flex; align-items: center; gap: 18px;
    font-size: 30px; font-weight: 700; letter-spacing: .5px;
    margin-bottom: 16px;
  }
  .contact-icon {
    width: 30px; height: 30px; flex: none;
    display: flex; align-items: center; justify-content: center;
  }
  .contact-dot { width: 26px; height: 26px; border-radius: 50%; background: var(--red); }
  .services {
    position: absolute; left: 60px; top: 290px; width: 800px;
    list-style: none;
    display: grid; grid-template-columns: 1fr 1fr; column-gap: 28px; row-gap: 10px;
  }
  .service {
    font-size: 17px; font-weight: 700; letter-spacing: .5px; text-transform: uppercase;
    display: flex; align-items: center; gap: 10px; white-space: nowrap;
  }
  .service::before {
    content: ""; width: 9px; height: 9px; background: var(--red);
    transform: rotate(45deg); flex: none;
  }
  .website {
    position: absolute; left: 60px; top: 418px;
    font-size: 24px; font-weight: 700; letter-spacing: .5px;
  }

  /* front */
  .brand {
    position: absolute; left: 0; right: 0; top: 120px;
    display: flex; flex-direction: column; align-items: center;
  }
  .brand-dot { width: 46px; height: 46px; border-radius: 50%; background: var(--white); margin-bottom: 54px; }
  .brand-name { font-size: 64px; font-weight: 800; letter-spacing: 1px; color: var(--white); line-height: 1; }
  .brand-role { font-size: 36px; font-weight: 500; letter-spacing: 1px; color: var(--red); margin-top: 12px; }
  .front-edge {
    position: absolute; right: 0; top: 0; width: 10px; height: 100%;
    background: var(--red);
  }
</style>
</head>
<body>

  <section class="card card--back" aria-label="Verso do cartão">
    <svg class="back-accent" viewBox="0 0 900 510" preserveAspectRatio="none" aria-hidden="true">
      <path d="M0 455 L340 455 L370 480 L900 480 L900 510 L0 510 Z" fill="#d8232a"/>
      <path d="M0 262 L520 262 L545 245 L900 245" stroke="#d8232a" stroke-width="3" fill="none"/>
    </svg>
    <div class="back-mark" aria-hidden="true"></div>
    <ul class="contact-list">
      <li class="contact-item">
        <span class="contact-icon">
          <svg width="28" height="28" viewBox="0 0 24 24" aria-hidden="true"><path fill="#d8232a" d="M6.6 10.8a15.1 15.1 0 0 0 6.6 6.6l2.2-2.2a1 1 0 0 1 1-.25 11.4 11.4 0 0 0 3.6.57 1 1 0 0 1 1 1V20a1 1 0 0 1-1 1A17 17 0 0 1 3 4a1 1 0 0 1 1-1h3.5a1 1 0 0 1 1 1c0 1.25.2 2.45.57 3.57a1 1 0 0 1-.25 1Z"/></svg>
        </span>
        (00) 90000-0000
      </li>
      <li class="contact-item"><span class="contact-icon"><span class="contact-dot"></span></span>/rafaelmoura</li>
      <li class="contact-item"><span class="contact-icon"><span class="contact-dot"></span></span>/rafaelmoura</li>
    </ul>
    <ul class="services">
      <li class="service">Emagrecimento</li>
      <li class="service">Hipertrofia</li>
      <li class="service">Condicionamento físico</li>
      <li class="service">Fortalecimento muscular</li>
      <li class="service">Melhora da capacidade funcional</li>
      <li class="service">Avaliação física</li>
      <li class="service">Assessoria esportiva</li>
    </ul>
    <p class="website">www.rafaelmoura.com.br</p>
  </section>

  <section class="card card--front" aria-label="Frente do cartão">
    <div class="front-edge" aria-hidden="true"></div>
    <div class="brand">
      <div class="brand-dot" aria-hidden="true"></div>
      <h1 class="brand-name">Rafael Moura</h1>
      <p class="brand-role">Personal Trainer</p>
    </div>
  </section>

</body>
</html>
```